Thornfield Marsh, LLC Website

We are a small law firm in need of a website that contains the following:
1. Attractive main page
2. About us/attorney info for three people: Leonard Thornfield (attorney), Brent Marsh (attorney), and Melinda Carrow (legal assistant). We have bio's ready to submit.
3. Blog/video page. We'd like to post blogs and videos to help drive traffic
4. Multidistrict Litigation and Class Actions page, where we post information regarding active MDLs and Class actions that we are doing intake on.
Updates

Can you also please use the color "gold" in the design and logo? Thanks.

Industry/Entity Type

Legal

Coding

Coded - Design and coding required

Number of Pages Required

1 page

Colors
0054AA
0677BA
7BADD7
CADEEF
E8F1F8

Requirements
Must have
• 1. Attractive main page 2. About us/attorney info for three people: Leonard Thornfield (attorney), Brent Marsh (attorney), and Melinda Carrow (legal assistant). We have bio's ready to submit. 3. Blog/video page. We'd like to post blogs and videos to help drive traffic 4. Multidistrict Litigation and Class Actions page, where we post information regarding active MDLs and Class actions that we are doing intake on.

```html
<!DOCTYPE html>
<html lang="en">
<head>
<meta charset="utf-8">
<title>Thornfield Marsh, LLC</title>
<link href="https://fonts.googleapis.com/css2?family=Jost:ital,wght@0,400;0,500;0,600;0,700;1,500&family=Open+Sans:wght@400;600&display=swap" rel="stylesheet">
<style>
:root{
  --blue:#0054AA;
  --blue-mid:#0677BA;
  --blue-soft:#7BADD7;
  --blue-pale:#CADEEF;
  --blue-mist:#E8F1F8;
  --navy:#0a3a78;
  --ink:#22324a;
  --grey:#6b7686;
  --white:#ffffff;
}
*{box-sizing:border-box;margin:0;padding:0}
html,body{width:1200px;height:4624px;overflow:hidden}
body{font-family:"Open Sans",Arial,sans-serif;color:var(--ink);background:var(--white);position:relative}
h1,h2,h3,h4,.nav,.btn,.brand{font-family:"Jost",Arial,sans-serif}
section,header,footer{position:relative;width:1200px}
.abs{position:absolute}
.btn{display:inline-block;font-size:13px;font-weight:600;letter-spacing:.06em;text-transform:uppercase;padding:14px 26px;border-radius:3px;white-space:nowrap}
.btn-blue{background:var(--blue);color:var(--white)}
.btn-white{background:var(--white);color:var(--blue)}
.more{font-family:"Jost",sans-serif;font-size:13px;font-weight:600;color:var(--blue);display:flex;align-items:center;gap:8px}
.more svg{width:16px;height:10px}

/* header */
.site-header{position:absolute;top:0;left:0;height:88px;background:var(--white);display:flex;align-items:center;padding:0 24px;z-index:5;box-shadow:0 2px 10px rgba(0,0,0,.08)}
.brand{display:flex;align-items:center;gap:10px;font-size:19px;font-weight:600;color:var(--blue);white-space:nowrap}
.brand-mark{width:22px;height:22px;background:var(--blue);flex:none}
.nav{display:flex;gap:28px;margin-left:70px;font-size:12.5px;font-weight:600;color:var(--navy);letter-spacing:.04em;white-space:nowrap}
.site-header .btn{margin-left:auto;padding:12px 20px;font-size:12px}

/* hero */
.hero{height:820px;background:linear-gradient(90deg,#0a4e9c 0%,#0a5fb0 45%,#3b83c6 100%);overflow:hidden}
.hero-photo{position:absolute;left:560px;top:88px;width:640px;height:700px;background:linear-gradient(135deg,#6d9fcf 0%,#b9cfe6 45%,#7aa7d4 100%)}
.hero-fade{position:absolute;left:560px;top:88px;width:260px;height:700px;background:linear-gradient(90deg,#0a5fb0,rgba(10,95,176,0))}
.hero-copy{position:absolute;left:52px;top:180px;color:var(--white)}
.hero-copy h1{font-size:54px;line-height:1.08;font-weight:700;text-transform:uppercase;width:500px}
.hero-copy p{font-size:17px;margin:28px 0 30px;font-weight:600}
.hero-wave{position:absolute;left:0;bottom:0;width:1200px;height:180px}

/* about */
.about{height:520px}
.about-back{left:124px;top:100px;width:400px;height:316px;background:var(--blue)}
.about-photo{left:140px;top:0;width:400px;height:320px;background:linear-gradient(160deg,#3a3530,#8d7a5f 55%,#2b2824)}
.about-copy{left:620px;top:10px;width:440px}
.about-copy h2{font-size:34px;font-weight:500;color:var(--navy);letter-spacing:.03em}
.tagline{font-family:"Jost",sans-serif;font-style:italic;font-weight:500;font-size:14px;color:var(--ink);margin:8px 0 26px;padding-bottom:6px;border-bottom:2px solid var(--blue);display:inline-block}
.about-copy p{font-size:13px;line-height:1.75;color:var(--grey);margin-bottom:14px}

/* attorneys */
.attorneys{height:620px;background:linear-gradient(180deg,rgba(6,84,170,.88),rgba(6,119,186,.82)),linear-gradient(90deg,#2d5f97,#6b93bf 50%,#2b5a8f)}
.section-title{font-size:32px;font-weight:600;letter-spacing:.03em;text-transform:uppercase;text-align:center}
.attorneys .section-title{position:absolute;top:100px;width:100%;color:var(--white)}
.title-rule{display:block;width:60px;height:3px;background:var(--blue-soft);margin:10px auto 0}
.attorney-card{top:176px;width:270px;height:366px;background:var(--white);box-shadow:0 8px 24px rgba(0,0,0,.2)}
.attorney-photo{height:156px;background:linear-gradient(180deg,#cfd8e2,#8e9fb2)}
.attorney-body{padding:16px 18px}
.attorney-body h3{font-size:19px;font-weight:600;color:var(--blue)}
.role{font-size:12px;color:var(--ink);margin:2px 0 10px}
.attorney-body p{font-size:11.5px;line-height:1.6;color:var(--grey);margin-bottom:14px}

/* mdl */
.mdl{height:900px}
.mdl .section-title{position:absolute;top:110px;width:100%;color:var(--blue);font-size:30px}
.mdl-grid{left:160px;top:180px;width:900px;height:540px;display:grid;grid-template-columns:300px 300px 300px;grid-template-rows:270px 270px}
.case-card{background:var(--white);padding:26px 24px;box-shadow:0 6px 22px rgba(10,58,120,.14);position:relative;z-index:2}
.case-card h3{font-size:17px;font-weight:600;color:var(--navy);margin-bottom:12px}
.case-card p{font-size:11.5px;line-height:1.65;color:var(--grey)}
.case-photo{width:100%;height:100%}
.p1{background:linear-gradient(135deg,#b8c7d6,#e6edf3 50%,#7a95b2)}
.p2{background:linear-gradient(135deg,#3f6286,#9fb6cb 55%,#5b7591)}
.p3{background:linear-gradient(135deg,#cfd9e4,#7c98b7)}
.mdl .btn{position:absolute;left:524px;top:770px}

/* testimonials */
.testimonials{height:480px;background:var(--blue-mist)}
.testimonials .section-title{position:absolute;top:100px;width:100%;color:var(--navy);font-size:30px}
.quote-card{top:176px;width:440px;height:240px;background:var(--white);padding:30px 28px;box-shadow:0 6px 20px rgba(10,58,120,.08)}
.quote-card p{font-size:12.5px;line-height:1.7;color:var(--grey)}
.client{display:flex;align-items:center;gap:14px;margin-top:26px}
.avatar{width:44px;height:44px;border-radius:50%;background:linear-gradient(135deg,#9ab2cb,#dbe5ef)}
.client span{font-family:"Jost",sans-serif;font-size:15px;font-weight:500;color:var(--blue)}
.arrow-btn{width:30px;height:30px;background:var(--white);display:flex;align-items:center;justify-content:center;box-shadow:0 2px 8px rgba(0,0,0,.1)}
.arrow-btn.solid{background:var(--blue)}
.dots{left:560px;top:444px;display:flex;gap:8px}
.dots i{width:8px;height:8px;border-radius:50%;background:var(--blue-pale)}
.dots i.on{background:var(--blue)}

/* insights */
.insights{height:700px}
.insights .section-title{position:absolute;top:120px;width:100%;color:var(--navy);font-size:30px}
.post-card{top:210px;width:280px;height:300px;background:var(--white);box-shadow:0 6px 22px rgba(10,58,120,.12)}
.post-photo{height:160px;position:relative}
.date{position:absolute;left:50%;transform:translateX(-50%);bottom:-12px;background:var(--blue);color:var(--white);font-size:11px;padding:5px 14px;white-space:nowrap}
.post-body{padding:28px 18px 0}
.post-body h3{font-family:"Open Sans",sans-serif;font-size:13.5px;font-weight:600;line-height:1.5;color:var(--ink);margin-bottom:14px}
.insights .btn{position:absolute;left:524px;top:566px}

/* footer */
.site-footer{height:584px;background:linear-gradient(180deg,#0a5fb0,#0054AA);color:var(--white)}
.footer-peak{position:absolute;top:0;left:0;width:1200px;height:90px}
.footer-brand{left:140px;top:150px;display:flex;align-items:center;gap:10px;font-size:18px;font-weight:600;color:var(--white);white-space:nowrap}
.footer-brand .brand-mark{background:var(--white)}
.f-col{top:150px}
.f-col h4{font-size:15px;font-weight:500;letter-spacing:.05em;margin-bottom:18px}
.f-col li{list-style:none;font-size:12px;margin-bottom:10px;display:flex;align-items:center;gap:12px}
.f-col .dot{width:22px;height:22px;border-radius:50%;background:rgba(255,255,255,.9);flex:none}
.f-col svg{width:22px;height:22px;flex:none}
.footer-base{left:140px;top:510px;width:920px;border-top:1px solid rgba(255,255,255,.35);padding-top:22px;display:flex;font-size:11.5px}
.footer-base .legal{margin-left:auto;display:flex;gap:60px}
</style>
</head>
<body>

<header class="site-header">
  <div class="brand"><span class="brand-mark"></span>Thornfield Marsh, LLC</div>
  <nav class="nav"><span>HOME</span><span>ABOUT US</span><span>ATTORNEYS</span><span>MULTIDISTRICT LITIGATION</span><span>INSIGHTS</span><span>CONTACT US</span></nav>
  <span class="btn btn-blue">Schedule Consultation</span>
</header>

<section class="hero">
  <div class="hero-photo" role="img" aria-label="Photo of a smiling family of three at home"></div>
  <div class="hero-fade"></div>
  <div class="hero-copy">
    <h1>Your Trusted Advocates in Legal Matters</h1>
    <p>Expertise in Multidistrict Litigation and Class Actions.</p>
    <span class="btn btn-white">Schedule a Consultation</span>
  </div>
  <svg class="hero-wave" viewBox="0 0 1200 180" preserveAspectRatio="none">
    <path d="M0 70 C300 160 700 40 1200 20 L1200 180 L0 180Z" fill="#0677BA" opacity=".7"/>
    <path d="M0 110 C320 175 720 70 1200 60 L1200 180 L0 180Z" fill="#7BADD7" opacity=".6"/>
    <path d="M0 130 C340 180 760 100 1200 95 L1200 180 L0 180Z" fill="#ffffff"/>
  </svg>
</section>

<section class="about">
  <div class="abs about-back"></div>
  <div class="abs about-photo" role="img" aria-label="Photo of brass scales of justice on a desk with a gavel"></div>
  <div class="abs about-copy">
    <h2>ABOUT US</h2>
    <span class="tagline">JUSTICE. INTEGRITY. COMMITMENT.</span>
    <p>At our firm, we are driven by one guiding principle: delivering justice with unwavering integrity and relentless commitment. With decades of combined experience, we specialize in complex litigation, including Multidistrict Litigation (MDL) and Class Action lawsuits. We represent clients nationwide, fighting tirelessly to hold corporations and institutions accountable.</p>
    <p>Leading the charge are our founding partners, seasoned trial lawyers with a long record of courtroom wins and settlements for injured clients. Their work has been recognized by peers, national rankings and regional legal publications across many years.</p>
  </div>
</section>

<section class="attorneys" role="img" aria-label="Blue tinted photo of a law office interior behind the attorney cards">
  <h2 class="section-title">Meet Our Attorneys<span class="title-rule"></span></h2>
  <article class="abs attorney-card" style="left:175px">
    <div class="attorney-photo" role="img" aria-label="Portrait of Leonard Thornfield"></div>
    <div class="attorney-body">
      <h3>Leonard Thornfield</h3><div class="role">Attorney</div>
      <p>Leonard has represented injured clients for decades, leading complex cases from first filing to final verdict with care.</p>
      <span class="more">Full Profile <svg viewBox="0 0 16 10"><path d="M0 5h14M10 1l4 4-4 4" stroke="#0054AA" stroke-width="1.6" fill="none"/></svg></span>
    </div>
  </article>
  <article class="abs attorney-card" style="left:465px">
    <div class="attorney-photo" role="img" aria-label="Portrait of Brent Marsh"></div>
    <div class="attorney-body">
      <h3>Brent Marsh</h3><div class="role">Attorney</div>
      <p>Brent focuses on mass torts and class actions, building strong cases against large companies for everyday families.</p>
      <span class="more">Full Profile <svg viewBox="0 0 16 10"><path d="M0 5h14M10 1l4 4-4 4" stroke="#0054AA" stroke-width="1.6" fill="none"/></svg></span>
    </div>
  </article>
  <article class="abs attorney-card" style="left:755px">
    <div class="attorney-photo" role="img" aria-label="Portrait of Melinda Carrow"></div>
    <div class="attorney-body">
      <h3>Melinda Carrow</h3><div class="role">Legal Assistant</div>
      <p>Melinda guides every new client through intake, keeping records organized and questions answered at each step.</p>
      <span class="more">Full Profile <svg viewBox="0 0 16 10"><path d="M0 5h14M10 1l4 4-4 4" stroke="#0054AA" stroke-width="1.6" fill="none"/></svg></span>
    </div>
  </article>
</section>

<section class="mdl">
  <h2 class="section-title">Multidistrict Litigation and Class Actions</h2>
  <div class="abs mdl-grid">
    <div class="case-card">
      <h3>Gastrolin Litigation</h3>
      <p>We are actively accepting clients who suffered health complications after prolonged use of Gastrolin heartburn medication. The recall of this product has opened the door for claims linked to a probable human carcinogen.</p>
    </div>
    <div class="case-photo p1" role="img" aria-label="Photo of a doctor reviewing an X-ray with a patient"></div>
    <div class="case-card">
      <h3>Camp Harlow Water Contamination</h3>
      <p>If you lived or worked at Camp Harlow between 1953 and 1987 and developed serious illness due to toxic water exposure, you may be eligible to file a claim under the new federal act.</p>
    </div>
    <div class="case-photo p2" role="img" aria-label="Photo of a doctor comforting a worried patient"></div>
    <div class="case-card" style="margin-top:-40px;height:310px">
      <h3>Orthaxis Joint Replacement Recall</h3>
      <p>Patients implanted with Orthaxis knee, hip or ankle devices are experiencing early failure and revision surgeries due to packaging defects.</p>
    </div>
    <div class="case-photo p3" role="img" aria-label="Photo of a hand holding a glass of tap water"></div>
  </div>
  <span class="btn btn-blue">Explore All</span>
</section>

<section class="testimonials">
  <h2 class="section-title">Our Customers About Us</h2>
  <div class="abs arrow-btn" style="left:72px;top:280px"><svg width="12" height="10" viewBox="0 0 12 10"><path d="M12 5H1M5 1 1 5l4 4" stroke="#0054AA" stroke-width="1.6" fill="none"/></svg></div>
  <div class="abs arrow-btn" style="left:1098px;top:280px"><svg width="12" height="10" viewBox="0 0 12 10"><path d="M0 5h11M7 1l4 4-4 4" stroke="#0054AA" stroke-width="1.6" fill="none"/></svg></div>
  <article class="abs quote-card" style="left:140px">
    <p>Overall great experience with the firm. Out-of-state probate matter was handled via email and phone and my calls were returned or answered right away. Peace of mind was worth it alone, thank you.</p>
    <div class="client"><span class="avatar" role="img" aria-label="Client photo"></span><span>Desmond Pryce</span></div>
  </article>
  <article class="abs quote-card" style="left:620px">
    <p>Probate matter was handled with care and diligence. I never felt uninformed throughout the entire ordeal. I can personally recommend this firm to anyone in the same boat as me in need of legal help involving probate.</p>
    <div class="client"><span class="avatar" role="img" aria-label="Client photo"></span><span>Rosalind Vega</span></div>
  </article>
  <div class="abs dots"><i></i><i></i><i class="on"></i><i></i><i></i></div>
</section>

<section class="insights">
  <h2 class="section-title">Latest Insights</h2>
  <div class="abs arrow-btn" style="left:66px;top:340px"><svg width="12" height="10" viewBox="0 0 12 10"><path d="M12 5H1M5 1 1 5l4 4" stroke="#0054AA" stroke-width="1.6" fill="none"/></svg></div>
  <div class="abs arrow-btn solid" style="left:1104px;top:340px"><svg width="12" height="10" viewBox="0 0 12 10"><path d="M0 5h11M7 1l4 4-4 4" stroke="#fff" stroke-width="1.6" fill="none"/></svg></div>
  <article class="abs post-card" style="left:140px">
    <div class="post-photo" style="background:linear-gradient(135deg,#c9d3de,#5f6f82)" role="img" aria-label="Photo of two lawyers reviewing documents at a desk"><span class="date">2 January 2025</span></div>
    <div class="post-body"><h3>Lorem Ipsum is simply dummy text of the printing &amp; type.</h3><span class="more">Read More <svg viewBox="0 0 16 10"><path d="M0 5h14M10 1l4 4-4 4" stroke="#0054AA" stroke-width="1.6" fill="none"/></svg></span></div>
  </article>
  <article class="abs post-card" style="left:460px">
    <div class="post-photo" style="background:linear-gradient(135deg,#2e2620,#9a7c55 55%,#3a3028)" role="img" aria-label="Photo of scales of justice and a gavel"><span class="date">3 January 2025</span></div>
    <div class="post-body"><h3>Lorem Ipsum is simply dummy text of the printing &amp; type.</h3><span class="more">Read More <svg viewBox="0 0 16 10"><path d="M0 5h14M10 1l4 4-4 4" stroke="#0054AA" stroke-width="1.6" fill="none"/></svg></span></div>
  </article>
  <article class="abs post-card" style="left:780px">
    <div class="post-photo" style="background:linear-gradient(135deg,#d7dfe8,#8ea2b8)" role="img" aria-label="Photo of a lawyer signing papers"><span class="date">3 January 2025</span></div>
    <div class="post-body"><h3>Lorem Ipsum is simply dummy text of the printing &amp; type.</h3><span class="more">Read More <svg viewBox="0 0 16 10"><path d="M0 5h14M10 1l4 4-4 4" stroke="#0054AA" stroke-width="1.6" fill="none"/></svg></span></div>
  </article>
  <span class="btn btn-blue">Explore All</span>
</section>

<footer class="site-footer">
  <svg class="footer-peak" viewBox="0 0 1200 90" preserveAspectRatio="none">
    <path d="M0 0 L1200 0 L1200 70 L600 0 L0 70Z" fill="#ffffff"/>
    <path d="M0 70 L600 0 L1200 70" stroke="#7BADD7" stroke-width="3" fill="none"/>
    <path d="M0 88 L600 18 L1200 88" stroke="#CADEEF" stroke-width="1.5" fill="none" opacity=".6"/>
  </svg>
  <div class="abs footer-brand"><span class="brand-mark"></span>Thornfield Marsh, LLC</div>
  <div class="abs f-col" style="left:416px">
    <h4>QUICK LINKS</h4>
    <ul><li>HOME</li><li>ABOUT US</li><li>ATTORNEYS</li><li>MULTIDISTRICT LITIGATION</li><li>INSIGHTS</li><li>CAREERS</li><li>CONTACT US</li></ul>
  </div>
  <div class="abs f-col" style="left:664px">
    <h4>SOCIAL MEDIA</h4>
    <ul><li><span class="dot"></span>Friendline</li><li><span class="dot"></span>Chirpnet</li><li><span class="dot"></span>Workring</li><li><span class="dot"></span>Vidwave</li></ul>
  </div>
  <div class="abs f-col" style="left:872px">
    <h4>CONTACT US</h4>
    <ul>
      <li><svg viewBox="0 0 22 22"><circle cx="11" cy="11" r="11" fill="#fff"/><path d="M7.5 6.5l2 0 1 2.5-1.3 1a6 6 0 0 0 2.8 2.8l1-1.3 2.5 1v2a1 1 0 0 1-1 1A8.5 8.5 0 0 1 6.5 7.5a1 1 0 0 1 1-1z" fill="#0054AA"/></svg>0221-555-0147</li>
      <li><svg viewBox="0 0 22 22"><circle cx="11" cy="11" r="11" fill="#fff"/><rect x="6" y="7.5" width="10" height="7" fill="none" stroke="#0054AA" stroke-width="1.3"/><path d="M6 7.5l5 4 5-4" fill="none" stroke="#0054AA" stroke-width="1.3"/></svg>info@thornfieldmarsh.com</li>
      <li><svg viewBox="0 0 22 22"><circle cx="11" cy="11" r="11" fill="#fff"/><path d="M11 5.5a4 4 0 0 1 4 4c0 3-4 7-4 7s-4-4-4-7a4 4 0 0 1 4-4z" fill="#0054AA"/><circle cx="11" cy="9.5" r="1.4" fill="#fff"/></svg>Lindenweg 48,<br>Harbor City</li>
    </ul>
  </div>
  <div class="abs footer-base">
    <span>Copyright © 2025 Thornfield Marsh - All Rights Reserved.</span>
    <div class="legal"><span>Privacy Policy</span><span>Terms of Service</span></div>
  </div>
</footer>

</body>
</html>
```